Steadfast Property Reviews

We need stationery for our new home inspection company. We inspect homes for people prior to purchasing to ensure the property is in good condition, as well as inspecting new homes to ensure they have been built to the appropriate standards. We are happy to look at combinations of colours. The use of a water mark would be good. Open to suggestions.

Industry/Entity Type

Home Inspection

```html
<!DOCTYPE html>
<html lang="en">
<head>
<meta charset="utf-8">
<title>Steadfast Property Reviews – Business Cards</title>
<link rel="stylesheet" href="https://fonts.googleapis.com/css2?family=Open+Sans:wght@300;400;600&display=swap">
<style>
  :root {
    --page-bg: #f3f3f3;
    --card-white: #ffffff;
    --slate: #8a949c;
    --brand-blue: #2b6a95;
    --ink: #4f5a63;
    --shadow: rgba(0, 0, 0, 0.12);
  }
  * { box-sizing: border-box; margin: 0; padding: 0; }
  html, body {
    width: 1200px; height: 1000px; overflow: hidden;
    background: var(--page-bg);
    font-family: "Open Sans", Arial, sans-serif;
  }
  .stationery {
    position: relative; width: 1200px; height: 1000px;
  }
  .card {
    position: absolute; left: 250px; width: 700px; height: 400px;
    background: var(--card-white);
    box-shadow: 0 18px 40px var(--shadow);
    overflow: hidden;
  }
  .card--back { top: 70px; display: flex; }
  .card--front { top: 530px; }

  /* Back card */
  .contact-side {
    width: 42%; padding: 54px 0 0 48px;
  }
  .company-name {
    color: var(--brand-blue); font-weight: 400;
    font-size: 21px; line-height: 1.25; display: flex; align-items: center; gap: 12px;
  }
  .company-name .brand-square {
    width: 30px; height: 30px; background: var(--brand-blue); flex: none;
  }
  .contact-list { list-style: none; margin-top: 40px; }
  .contact-list li {
    display: flex; align-items: flex-start; gap: 12px;
    color: var(--ink); font-size: 13px; line-height: 1.35; margin-bottom: 11px;
  }
  .contact-list svg { width: 14px; height: 14px; flex: none; margin-top: 2px; fill: var(--brand-blue); }

  .name-side {
    width: 58%; background: var(--slate); position: relative;
    display: flex; flex-direction: column; justify-content: center; padding-left: 60px;
    border-right: 10px solid var(--brand-blue);
  }
  .person-name { color: #fff; font-weight: 300; font-size: 42px; line-height: 1.1; }
  .person-title { color: #fff; font-weight: 400; font-size: 15px; margin-top: 6px; }

  /* Front card */
  .front-name {
    position: absolute; left: 110px; top: 150px;
    color: var(--brand-blue); font-weight: 300; font-size: 44px; line-height: 1.15;
  }
  .edge-band {
    position: absolute; top: 0; right: 0; height: 100%; width: 40px;
    border-left: 10px solid var(--brand-blue); background: var(--slate);
  }
</style>
</head>
<body>
<main class="stationery">

  <section class="card card--back" aria-label="Business card back">
    <div class="contact-side">
      <h1 class="company-name"><span class="brand-square"></span><span>Steadfast<br>Property Reviews</span></h1>
      <ul class="contact-list">
        <li>
          <svg viewBox="0 0 24 24" aria-hidden="true"><path d="M12 2a7 7 0 0 0-7 7c0 5 7 13 7 13s7-8 7-13a7 7 0 0 0-7-7zm0 9.5A2.5 2.5 0 1 1 12 6.5a2.5 2.5 0 0 1 0 5z"/></svg>
          <span>48 Elm Row, Brookfield,<br>Postal Code, Country</span>
        </li>
        <li>
          <svg viewBox="0 0 24 24" aria-hidden="true"><path d="M6.6 10.8a15 15 0 0 0 6.6 6.6l2.2-2.2a1 1 0 0 1 1-.25 11.4 11.4 0 0 0 3.6.57 1 1 0 0 1 1 1V20a1 1 0 0 1-1 1A17 17 0 0 1 3 4a1 1 0 0 1 1-1h3.5a1 1 0 0 1 1 1c0 1.25.2 2.45.57 3.57a1 1 0 0 1-.25 1z"/></svg>
          <span>555-0182-40</span>
        </li>
        <li>
          <svg viewBox="0 0 24 24" aria-hidden="true"><path d="M3 5h18v14H3zm2 2v.4l7 4.6 7-4.6V7zm0 2.8V17h14V9.8l-7 4.6z"/></svg>
          <span>hello@steadfastreviews.com</span>
        </li>
        <li>
          <svg viewBox="0 0 24 24" aria-hidden="true"><path d="M12 2a10 10 0 1 0 0 20 10 10 0 0 0 0-20zm6.9 6h-2.9a15.7 15.7 0 0 0-1.4-3.6A8 8 0 0 1 18.9 8zM12 4c.8 1.2 1.5 2.5 1.9 4h-3.8c.4-1.5 1.1-2.8 1.9-4zM4.3 14a8 8 0 0 1 0-4h3.4a16 16 0 0 0 0 4zm.8 2h2.9c.3 1.3.8 2.5 1.4 3.6A8 8 0 0 1 5.1 16zM8 8H5.1a8 8 0 0 1 4.3-3.6C8.8 5.5 8.3 6.7 8 8zm4 12c-.8-1.2-1.5-2.5-1.9-4h3.8c-.4 1.5-1.1 2.8-1.9 4zm2.3-6H9.7a14.7 14.7 0 0 1 0-4h4.6a14.7 14.7 0 0 1 0 4zm.3 5.6c.6-1.1 1.1-2.3 1.4-3.6h2.9a8 8 0 0 1-4.3 3.6zm1.7-5.6a16 16 0 0 0 0-4h3.4a8 8 0 0 1 0 4z"/></svg>
          <span>www.steadfastreviews.com</span>
        </li>
      </ul>
    </div>
    <div class="name-side">
      <h2 class="person-name">Daniel Hartley</h2>
      <p class="person-title">Chief Executive Manager</p>
    </div>
  </section>

  <section class="card card--front" aria-label="Business card front">
    <h2 class="front-name">Steadfast<br>Property Reviews</h2>
    <div class="edge-band"></div>
  </section>

</main>
</body>
</html>
```